Bramwell Electrical Services Website

'Fennimore Electrical Services' is a leading electrician company based in Hertfordshire. We are a QUORVIN approved and registered company in the UK. We are also registered to carry out electrical installations under Part P of the building regulations. As part of a wide range of electrical services, we have professional expertise in installation testing (landlords, periodic, insurance, emergency lighting & fire alarms) rewires, installations, electrical maintenance, security systems & portable appliance testing (PAT). We provide a bespoke service to suite the needs of High End clients so the site must reflect the type of clientele we are targeting

WE ARE A SMALL COMPANY AND ARE LOOKING FOR THE DESIGNERS TO ALSO IMPLEMENT THIS ONTO OUR DOMAIN NAME SO ITS A FULLY FUNCTIONAL FOR OUR CLIENTS WHEN WE FINISH THIS SIMPLE PROJECT

Target Market(s)

Estate Agents, High End Clients that require intallations in Multi Million pound houses

Industry/Entity Type

Electrician

Font styles to use
Serif
Sans Serif
Other font styles liked:
• Chose an elegant professional font

Requirements
Must have
• please look at www.fennimoreelectrical.co.uk (the current old site is down, and will go live in 24-48 hours so please get the content from there)

Luxury design, a wow factor when high end clients logon

the logo is Blue so a blue colour these for the branding is essential. We are open to your design ideas around the logo.

QUORVIN and Part P and Circuit Assurance Guild are safety regulations so please add the logos a place on the site together.
Nice to have
• your creative input
Should not have
• to many conflicting colours, too many horrible bright colours

```html
<!DOCTYPE html>
<html lang="en">
<head>
<meta charset="utf-8">
<title>Fennimore Electrical Services – Contact</title>
<link href="https://fonts.googleapis.com/css2?family=Lato:wght@300;400;700;900&display=swap" rel="stylesheet">
<style>
  :root{
    --header-bg:#f5f5f5;
    --page-bg:#ffffff;
    --ink:#222222;
    --heading:#4a4a4a;
    --muted:#9a9a9a;
    --body:#555555;
    --field-bg:#f7f7f7;
    --field-border:#e2e2e2;
    --accent:#3a6ad8;
    --link:#e0504a;
    --footer-bg:#0b1a4b;
    --copyright-bg:#1c3b9c;
    --map-land:#ece8dc;
    --white:#ffffff;
  }
  *{box-sizing:border-box;margin:0;padding:0}
  html,body{width:1099px;height:1200px;overflow:hidden}
  body{font-family:'Lato',sans-serif;background:var(--page-bg);color:var(--ink);position:relative}

  .site-header{position:absolute;left:0;top:0;width:1099px;height:102px;background:var(--header-bg)}
  .brand-name{position:absolute;left:176px;top:34px;font-weight:700;font-size:22px;line-height:26px;color:var(--ink)}
  .main-nav{position:absolute;top:79px;right:172px;display:flex;align-items:center;gap:22px;font-size:13.5px;font-weight:700;color:var(--ink)}
  .main-nav .dot{width:4px;height:4px;border-radius:50%;background:#777}
  .main-nav .current{color:var(--accent)}

  .intro{position:absolute;left:174px;top:132px;width:752px;text-align:center}
  .intro h1{font-size:21px;font-weight:700;color:var(--heading)}
  .intro p{margin-top:6px;font-size:17.5px;font-weight:300;color:var(--muted);line-height:21px;text-align:justify;text-align-last:center}

  .location-map{position:absolute;left:169px;top:247px;width:762px;height:308px;background:linear-gradient(160deg,var(--map-land),#e2e6d2 55%,var(--map-land))}

  .contact-form{position:absolute;left:169px;top:580px;width:564px}
  .contact-form h2{font-size:16px;font-weight:700;color:var(--heading)}
  .contact-form p{margin-top:9px;font-size:10px;color:var(--body);line-height:16px}
  .field-row{display:flex;gap:11px;margin-top:16px}
  .field{height:25px;background:var(--field-bg);border:1px solid var(--field-border);font-size:9.5px;color:#aaa;padding:6px 7px}
  .field.name,.field.email,.field.subject{width:180px}
  .field.message{margin-top:10px;width:564px;height:137px}
  .submit{position:absolute;left:4px;top:269px;width:83px;height:33px;background:var(--accent);border-radius:4px;color:var(--white);font-size:12px;font-weight:700;display:flex;align-items:center;justify-content:center}

  .address{position:absolute;left:763px;top:582px;width:162px;font-size:10px;color:var(--body)}
  .address h3{font-size:11px;font-weight:700;color:var(--heading)}
  .address p{margin-top:14px;line-height:16.3px}
  .address ul{list-style:none;margin-top:18px}
  .address li{display:flex;align-items:center;gap:8px;height:16.5px;white-space:nowrap}
  .address li a{color:var(--link);text-decoration:none}
  .address svg{width:9px;height:9px;fill:#555;flex:none}

  .site-footer{position:absolute;left:0;top:912px;width:1099px;height:232px;background:var(--footer-bg);color:var(--white);text-align:center}
  .site-footer h2{margin-top:28px;font-size:30px;font-weight:700}
  .site-footer .lead{margin-top:12px;font-size:19.5px;font-weight:300}
  .footer-contact{margin-top:16px;display:flex;justify-content:center;gap:30px;font-size:14px}
  .footer-contact span{display:flex;align-items:center;gap:8px}
  .footer-contact svg{width:11px;height:11px;fill:var(--white)}
  .social{margin-top:26px;display:flex;justify-content:center;gap:7px}
  .social span{width:29px;height:29px;border-radius:50%}
  .social .s1{background:#f2a94a}.social .s2{background:#4a6fc0}.social .s3{background:#4fa6e0}.social .s4{background:#e88fb7}.social .s5{background:#d9454a}
  .copyright{position:absolute;left:0;top:1144px;width:1099px;height:56px;background:var(--copyright-bg);color:var(--white);font-size:13.5px;display:flex;align-items:center;justify-content:center}
</style>
</head>
<body>
  <header class="site-header">
    <div class="brand-name">Fennimore Electrical Services</div>
    <nav class="main-nav">
      <span>HOME</span><span class="dot"></span>
      <span>ABOUT US</span><span class="dot"></span>
      <span>SERVICES</span><span class="dot"></span>
      <span>QUALITY</span><span class="dot"></span>
      <span class="current">CONTACT</span>
    </nav>
  </header>

  <section class="intro">
    <h1>Get in Touch</h1>
    <p>Fusce dapibus, tellus ac cursus commodo, tortor mauris condimentum. Duis mollis, est non commodo luctus, nisi erat porttitor ligula, eget lacinia odio sem nec elit. Fusce dapibus, tellus ac cursus commodo, tortor mauris condimentum nibh.</p>
  </section>

  <div class="location-map" role="img" aria-label="Street map showing the company location beside the river"></div>

  <section class="contact-form">
    <h2>Feel Free to Drop Us a Line</h2>
    <p>Maecenas vehicula condimentum consequat. Ut suscipit ipsum eget leotero convallis feugiat upsoyut fermentum leo auctor consequat turpis aturo nisiper.</p>
    <div class="field-row">
      <div class="field name">Name (Required)</div>
      <div class="field email">Email (Required)</div>
      <div class="field subject">Subject</div>
    </div>
    <div class="field message"></div>
    <div class="submit">SUBMIT</div>
  </section>

  <aside class="address">
    <h3>Address</h3>
    <p>Fusce dapibus, tellus commodo, tortor mauris condimentum utellus fermentum, porta sem malesuada magna. Sed posuere consectetur est at lobortis. Morbi leo risus, porta ac consectetur.</p>
    <ul>
      <li><svg viewBox="0 0 10 10"><path d="M5 0a3.5 3.5 0 0 0-3.5 3.5C1.5 6 5 10 5 10s3.5-4 3.5-6.5A3.5 3.5 0 0 0 5 0zm0 5a1.4 1.4 0 1 1 0-2.8A1.4 1.4 0 0 1 5 5z"/></svg>Larkfield Rd. 22/07 Hollowmere</li>
      <li><svg viewBox="0 0 10 10"><path d="M2 0l2 2.5-1.2 1.3a6 6 0 0 0 3.4 3.4L7.5 6 10 8 8.5 10C4 9.5.5 6 0 1.5z"/></svg>0193 628 40 15</li>
      <li><svg viewBox="0 0 10 10"><path d="M0 2h10v6H0zM0 2l5 3.5L10 2" stroke="#fff" stroke-width=".8"/></svg><a>hello@fennimoreelectrical.co.uk</a></li>
    </ul>
  </aside>

  <footer class="site-footer">
    <h2>Get in Touch</h2>
    <p class="lead">Vestibulum id ligula porta felis euismod semper,malesuada euismod.</p>
    <div class="footer-contact">
      <span><svg viewBox="0 0 10 10"><path d="M5 0a3.5 3.5 0 0 0-3.5 3.5C1.5 6 5 10 5 10s3.5-4 3.5-6.5A3.5 3.5 0 0 0 5 0zm0 5a1.4 1.4 0 1 1 0-2.8A1.4 1.4 0 0 1 5 5z"/></svg>Larkfield Road 22/07, Hollowmere, England</span>
      <span><svg viewBox="0 0 10 10"><path d="M2 0l2 2.5-1.2 1.3a6 6 0 0 0 3.4 3.4L7.5 6 10 8 8.5 10C4 9.5.5 6 0 1.5z"/></svg>0193 628 40 15</span>
    </div>
    <div class="social">
      <span class="s1"></span><span class="s2"></span><span class="s3"></span><span class="s4"></span><span class="s5"></span>
    </div>
  </footer>
  <div class="copyright">@ 2013 Copyright FENNIMORE ELECTRICAL SERVICES</div>
</body>
</html>
```